Paleo Diet Book Cover Design

I need a cover designed for my book Stone Frame that will be sold on Rivora Pageleaf and other sites. So the front, side and back will need to be designed. I have attached part of the book here so feel free to skim through the content and give it a quick read to get a feel for what the book is about. Stone Frame is about eating the diet of the caveman (paleolithic era-paleo) and a 12 week workout plan with a grocery shopping list and meal plans. It is for men and women ages 18+ who are interested in health and fitness and becoming healthier overall.
The graphics should be secondary, and it should add to the text, not distract from it. This is even more important because the size of the cover displayed on Rivora/Pageleaf, when your book is first seen by a potential buyer, is so tiny. It's barely an inch high, and even smaller in width.
So the words have to be big, bold, benefit-rich and easy to read. That also means, don't mess with the fancy fonts. Clean, clear, crisp font is best. And, did I say BIG already?
Contrast the colors of the text and background, so its even easier to read. That means, dark text on light background or visa versa. Colors like darker reds, blues / teals and oranges.
Please read this: http://www.bookvantrel.com/8-cover-design-secrets-publishers-use-to-manipulate-readers-into-buying-books/
The cover has to be bold and easy to read, it has to stick out, it has to draw the attention of your readers so that they zero in on my book, out of all the other books on the page. (Much like they would when viewing a classified ads site/page.)
The Title of the Book is Stone Frame, and the subtitle is "Transform Your Body For Life in 12 Weeks With Proven Workouts and Paleo Diet Based Nutrition" Perhaps “Transform Your Body For Life in 12 Weeks” could also be in a large font similar to the title with the rest of the subtitle following afterwards. You can try having the title be the smaller font with the subtitle being the larger font as well.
Then the authors name "Colin Marsh” incorporated into the design.
I am not sure what to use as the background type of design for the front of the book so feel free to be creative with that.
The size needs to be 1563 pixels on the shortest side and 2500 pixels on the longest side just for the front of the cover.

```html
<!DOCTYPE html>
<html lang="en">
<head>
<meta charset="utf-8">
<title>Stone Frame – Book Cover</title>
<link href="https://fonts.googleapis.com/css2?family=Londrina+Solid:wght@900&family=Rubik:wght@700&display=swap" rel="stylesheet">
<style>
  :root {
    --board: #ffffff;
    --bark: #43291a;
    --amber: #f29100;
    --amber-deep: #d97f00;
    --cream: #ffffff;
  }
  html, body {
    margin: 0;
    padding: 0;
    width: 1200px;
    height: 1000px;
    overflow: hidden;
    background: var(--board);
  }
  .board {
    position: relative;
    width: 1200px;
    height: 1000px;
    background: var(--board);
  }
  .board__rule {
    position: absolute;
    left: 0; top: 0;
    width: 1200px; height: 8px;
    background: var(--bark);
  }
  .cover {
    position: absolute;
    width: 406px;
    height: 649px;
    background: var(--amber);
    overflow: hidden;
    transform-origin: 0 0;
  }
  .cover--full { left: 390px; top: 212px; }
  .cover--thumb { left: 544px; top: 28px; transform: scale(0.2463); }

  .cover__author, .cover__title {
    position: absolute;
    left: 0; top: 0;
    width: 406px;
    overflow: visible;
  }
  .cover__author text {
    font-family: 'Londrina Solid', 'Arial Black', sans-serif;
    font-weight: 900;
    fill: var(--cream);
  }
  .cover__title text {
    font-family: 'Londrina Solid', 'Arial Black', sans-serif;
    font-weight: 900;
    fill: var(--bark);
  }
  .cover__art {
    position: absolute;
    left: 0; top: 258px;
    width: 392px; height: 222px;
    background: linear-gradient(160deg, var(--bark) 0%, #6b4a32 45%, #f4f4f4 75%, var(--amber-deep) 100%);
    opacity: 0.9;
  }
  .cover__band {
    position: absolute;
    left: 0; top: 500px;
    width: 406px; height: 118px;
    background: var(--bark);
  }
  .cover__subtitle {
    position: absolute;
    left: 16px; top: 12px;
    width: 385px;
    margin: 0;
    font-family: 'Rubik', 'Arial', sans-serif;
    font-weight: 700;
    font-size: 20.5px;
    line-height: 25px;
    letter-spacing: 0.6px;
    text-transform: uppercase;
    color: var(--amber);
  }
</style>
</head>
<body>
<div class="board">
  <div class="board__rule"></div>

  <div class="cover cover--thumb" aria-hidden="true">
    <svg class="cover__author" height="60" viewBox="0 0 406 60">
      <text x="16" y="48" font-size="46" textLength="375" lengthAdjust="spacingAndGlyphs">COLIN MARSH</text>
    </svg>
    <svg class="cover__title" height="260" viewBox="0 0 406 260">
      <text x="14" y="144" font-size="122" textLength="378" lengthAdjust="spacingAndGlyphs">STONE</text>
      <text x="14" y="248" font-size="122" textLength="378" lengthAdjust="spacingAndGlyphs">FRAME</text>
    </svg>
    <div class="cover__art"></div>
    <div class="cover__band">
      <p class="cover__subtitle">Transform your body for life in 12 weeks with proven workouts and paleo diet based nutrition.</p>
    </div>
  </div>

  <div class="cover cover--full">
    <svg class="cover__author" height="60" viewBox="0 0 406 60">
      <text x="16" y="48" font-size="46" textLength="375" lengthAdjust="spacingAndGlyphs">COLIN MARSH</text>
    </svg>
    <svg class="cover__title" height="260" viewBox="0 0 406 260">
      <text x="14" y="144" font-size="122" textLength="378" lengthAdjust="spacingAndGlyphs">STONE</text>
      <text x="14" y="248" font-size="122" textLength="378" lengthAdjust="spacingAndGlyphs">FRAME</text>
    </svg>
    <div class="cover__art" role="img" aria-label="Illustration of a hairy caveman arm reaching down to a white dinner plate"></div>
    <div class="cover__band">
      <p class="cover__subtitle">Transform your body for life in 12 weeks with proven workouts and paleo diet based nutrition.</p>
    </div>
  </div>
</div>
</body>
</html>
```